Visitenkarten-Design für Recommerce Unternehmen
Zielgruppe
Recommerce Unternehmen für Porzellan, Glas, Besteck. Wir handeln mit hochwertigen ausgelaufenen Artikeln und ermöglichen unseren Kunden den Nachkauf gesuchter Stücke.
Aufgabenstellung
Möglichst gleiches Look and Feel von der Homepage verwenden, aber darf gern ein wenig Frische reinbringen.

```html
<!DOCTYPE html>
<html lang="de">
<head>
<meta charset="utf-8">
<title>Visitenkarte – Porzellanbörse tassenfund.de</title>
<link href="https://fonts.googleapis.com/css2?family=Kalam:wght@700&family=Roboto:wght@400;700&display=swap" rel="stylesheet">
<style>
  :root {
    --card-bg: #46484c;
    --pattern-tone: #4d4f54;
    --lettering-tone: #8e9095;
    --text-light: #ffffff;
  }
  html, body {
    margin: 0;
    padding: 0;
    width: 1200px;
    height: 777px;
    overflow: hidden;
    background: var(--card-bg);
  }
  .card {
    position: relative;
    width: 1200px;
    height: 777px;
    background: var(--card-bg);
    color: var(--text-light);
    font-family: "Roboto", Arial, sans-serif;
    overflow: hidden;
  }
  .backdrop-pattern {
    position: absolute;
    inset: 0;
    width: 100%;
    height: 100%;
  }
  .slogan-lettering {
    position: absolute;
    left: 108px;
    top: 72px;
    width: 986px;
    height: 156px;
  }
  .tagline {
    position: absolute;
    left: 0;
    right: 0;
    top: 334px;
    margin: 0;
    text-align: center;
    font-family: "Kalam", cursive;
    font-weight: 700;
    font-size: 37px;
    line-height: 1;
  }
  .address {
    position: absolute;
    left: 126px;
    top: 452px;
    font-size: 30px;
    line-height: 44px;
    font-style: normal;
  }
  .company-name {
    display: block;
    font-weight: 700;
  }
  .phone-lines {
    position: absolute;
    left: 126px;
    top: 620px;
    font-size: 30px;
    line-height: 48px;
  }
  .web-lines {
    position: absolute;
    right: 124px;
    top: 620px;
    font-size: 30px;
    line-height: 48px;
    text-align: right;
  }
  .phone-lines p, .web-lines p { margin: 0; }
</style>
</head>
<body>
<div class="card">
  <svg class="backdrop-pattern" role="img" aria-label="Dezentes Ornamentmuster im Hintergrund" viewBox="0 0 1200 777" preserveAspectRatio="none">
    <defs>
      <radialGradient id="pattern-glow" cx="50%" cy="45%" r="70%">
        <stop offset="0" stop-color="var(--pattern-tone)"/>
        <stop offset="1" stop-color="var(--card-bg)"/>
      </radialGradient>
    </defs>
    <rect width="1200" height="777" fill="url(#pattern-glow)"/>
  </svg>

  <svg class="slogan-lettering" role="img" aria-label="Handgeschriebener Slogan in weißer Pinselschrift" viewBox="0 0 986 156">
    <rect width="986" height="156" rx="18" fill="var(--lettering-tone)" opacity="0.45"/>
  </svg>

  <p class="tagline">Wir kaufen Ihr altes Porzellan, Glaswaren und Besteck</p>

  <address class="address">
    <span class="company-name">Porzellanbörse tassenfund.de GmbH</span>
    Lindenweg 57<br>
    24537 Halmbrück
  </address>

  <div class="phone-lines">
    <p>Tel.: 040 718 36 52 - 00</p>
    <p>Fax: 040 718 36 52 - 29</p>
  </div>

  <div class="web-lines">
    <p>info@tassenfund.de</p>
    <p>www.tassenfund.de</p>
  </div>
</div>
</body>
</html>
```